Weight Loss Flyer

We are looking to get a flyer designed for our home consultant weight loss business. We call to customers homes and sell our meal replacement shakes, soups and bars and give nutrition and diet advice. We are mobile weight loss consultants. Our company is "The Slim Path Circle". We provide a free initial consultation which usually costs €30. We want the flyer to draw attention to our service and to contact us to help them lose weight.
We need an A4, A5, DL size flyers
Target Market(s)
Target audience is females between 30-60 years who want to lose weight and may have tried trim keepers, molly brandt etc...
Industry/Entity Type
Nutrition
Look and feel

```html
<!DOCTYPE html>
<html lang="en">
<head>
<meta charset="utf-8">
<title>The Slim Path Circle – Flyer</title>
<link href="https://fonts.googleapis.com/css2?family=Archivo+Black&family=Arimo:ital,wght@0,400;0,700;1,700&family=Lora:ital,wght@0,700;1,700&display=swap" rel="stylesheet">
<style>
  :root {
    --green: #1f8a3a;
    --green-dark: #12652a;
    --orange: #f28a1e;
    --orange-light: #fbb25a;
    --orange-deep: #e4701a;
    --ink: #1e1e1e;
    --white: #ffffff;
    --cream: #fff6ea;
  }
  * { margin: 0; padding: 0; box-sizing: border-box; }
  html, body { width: 851px; height: 1200px; overflow: hidden; }
  body { font-family: "Arimo", Arial, sans-serif; color: var(--ink); background: var(--white); }

  .flyer {
    position: relative; width: 851px; height: 1200px; overflow: hidden;
    background: radial-gradient(ellipse 560px 520px at 120px 220px, var(--orange-light) 0%, #fde1b8 45%, var(--white) 80%);
  }

  .hero-photo {
    position: absolute; left: 440px; top: 0; width: 411px; height: 667px;
    background: linear-gradient(160deg, #f3d3c0 0%, #e9a7b3 45%, #e0517e 75%, #f0c4ae 100%);
  }

  .brand { position: absolute; left: 40px; top: 40px; width: 440px; }
  .brand-name {
    font-family: "Archivo Black", Arial, sans-serif; color: var(--green);
    font-size: 74px; line-height: 1; text-transform: uppercase; letter-spacing: -1px;
  }
  .brand-tape {
    margin: 14px 0 0 4px; width: 420px; height: 44px; border-radius: 4px;
    background: linear-gradient(180deg, #f9e27a 0%, #f1c83a 100%);
  }

  .intro { position: absolute; left: 28px; top: 390px; width: 510px; font-size: 16px; line-height: 1.38; }
  .intro-wrap { float: right; width: 110px; height: 285px; }
  .intro p { margin-bottom: 14px; }
  .intro strong { font-weight: 700; }
  .intro .caps { text-transform: uppercase; font-weight: 700; }

  .offer-title {
    position: absolute; left: 28px; top: 842px; width: 500px; text-align: center;
    font-family: "Arimo", Arial, sans-serif; font-style: italic; font-weight: 700;
    font-size: 44px; color: var(--orange-deep);
  }
  .offer-box {
    position: absolute; left: 28px; top: 900px; width: 500px; height: 112px;
    background: var(--green); color: var(--white); border-radius: 22px;
    display: flex; align-items: center; justify-content: center; text-align: center;
    font-size: 20px; font-weight: 700; line-height: 1.3; padding: 0 22px;
  }

  .contact-band {
    position: absolute; left: 0; top: 1030px; width: 540px; height: 170px;
    background: linear-gradient(180deg, var(--orange) 0%, var(--orange-deep) 100%);
    color: var(--white); text-align: center; padding-top: 28px;
  }
  .contact-label { font-size: 18px; font-weight: 700; text-transform: uppercase; }
  .contact-phone { display: inline-flex; align-items: center; gap: 14px; margin-top: 16px;
    font-family: "Archivo Black", Arial, sans-serif; font-size: 52px; letter-spacing: 1px; white-space: nowrap; }
  .contact-phone svg { width: 40px; height: 40px; }

  .daily-diet {
    position: absolute; left: 552px; top: 667px; width: 285px; height: 533px;
    background: var(--cream); border: 3px solid var(--orange); text-align: center;
  }
  .diet-header {
    background: var(--orange); color: var(--white); font-family: "Lora", Georgia, serif;
    font-weight: 700; font-size: 32px; padding: 10px 0; letter-spacing: 1px;
  }
  .meal { padding: 16px 18px 0; }
  .meal h3 { font-family: "Lora", Georgia, serif; font-style: italic; font-size: 26px; color: var(--green-dark); }
  .meal p { font-size: 15px; line-height: 1.35; margin-top: 4px; }
</style>
</head>
<body>
<main class="flyer">
  <div class="hero-photo" role="img" aria-label="Smiling woman in a pink top measuring her slim waist with a tape measure"></div>

  <header class="brand">
    <h1 class="brand-name">The Slim Path Circle</h1>
    <div class="brand-tape" role="img" aria-label="Yellow measuring tape ribbon"></div>
  </header>

  <section class="intro">
    <div class="intro-wrap"></div>
    <p><strong>The Slim Path Circle</strong> are professionally trained Consultants who provide weekly one on one support, combined with a personalised and easy to follow weight loss solution - All in the convenience of your home, workplace or a location that suits you.</p>
    <p>Yes we are mobile - <strong>We come to you!</strong></p>
    <p><strong>The Slim Path Circle</strong> use a great tasting range of healthy meal options, meal replacement shakes and soup, low calorie snack and portion controlled meals.</p>
    <p>As well as fantastic personal one-on-one support from your Consultant, you will also gain access to your very own personalised 24 hour online support.</p>
    <p>Make the call today and <span class="caps">The Slim Path Circle</span> can start with you today!</p>
  </section>

  <h2 class="offer-title">Exclusive Offer</h2>
  <div class="offer-box">Receive a FREE initial weight loss consultation at home worth €30 and make the change to a healthier, happier new you.</div>

  <footer class="contact-band">
    <p class="contact-label">The Slim Path Circle customer care info line:</p>
    <p class="contact-phone">
      <svg viewBox="0 0 24 24" aria-hidden="true"><path fill="#ffffff" d="M6.6 10.8c1.4 2.8 3.8 5.1 6.6 6.6l2.2-2.2c.3-.3.7-.4 1-.2 1.1.4 2.3.6 3.6.6.6 0 1 .4 1 1V20c0 .6-.4 1-1 1C10.6 21 3 13.4 3 4c0-.6.4-1 1-1h3.5c.6 0 1 .4 1 1 0 1.3.2 2.5.6 3.6.1.3 0 .7-.2 1l-2.3 2.2z"/></svg>
      021.555.0147
    </p>
  </footer>

  <aside class="daily-diet">
    <div class="diet-header">DAILY DIET</div>
    <div class="meal"><h3>Breakfast</h3><p>One Meal Replacement Shake</p></div>
    <div class="meal"><h3>Lunch</h3><p>One Meal Replacement Shake or Soup</p></div>
    <div class="meal"><h3>Dinner</h3><p>One piece of grilled steak or steamed fish and salad alternated with one of our healthy option meals</p></div>
    <div class="meal"><h3>Snacks</h3><p>A serving of low fat yogurt or a piece of fruit or a snack from our list</p></div>
  </aside>
</main>
</body>
</html>
```